Brindlequest.com is a mountain biking and climbing travel company. We need a advertisement fo...

We need a advertisement for the back cover of a guide book. We would like a simple but strong ad that includes our logo. It must state that we are a biking and climbing company and people can contact us at the web site brindlequest.com We would like you to incorparate and below photo and logo on the ad.

```html
<!DOCTYPE html>
<html lang="en">
<head>
<meta charset="utf-8">
<title>Brindlequest Tours – Back Cover Ad</title>
<link href="https://fonts.googleapis.com/css2?family=Michroma&family=Open+Sans:wght@600&display=swap" rel="stylesheet">
<style>
  :root {
    --backdrop: #a1a1a1;
    --ink-white: #ffffff;
    --band-dark: #2a2a2a;
    --logo-top: #1b1b1b;
    --logo-mid: #3a3a3a;
    --photo-sky: #6f7b52;
    --photo-wall: #e6dccb;
    --photo-glow: #c99a55;
    --photo-street: #8e8a85;
    --photo-stone: #6f6d6b;
  }
  html, body {
    margin: 0;
    width: 1200px;
    height: 1200px;
    overflow: hidden;
    background: var(--backdrop);
  }
  .ad {
    position: absolute;
    left: 201px;
    top: 40px;
    width: 798px;
    height: 1120px;
    overflow: hidden;
  }
  .ad__photo {
    position: absolute;
    inset: 0 0 128px 0;
    background:
      radial-gradient(ellipse 30% 22% at 45% 48%, rgba(240,170,80,0.55), transparent 70%),
      linear-gradient(90deg, rgba(210,170,120,0.35) 0%, transparent 30%, transparent 70%, rgba(240,236,228,0.5) 100%),
      linear-gradient(180deg, var(--photo-wall) 0%, var(--photo-sky) 22%, var(--photo-wall) 36%, var(--photo-glow) 54%, var(--photo-street) 72%, var(--photo-stone) 100%);
  }
  .ad__logo-box {
    position: absolute;
    left: 246px;
    top: 0;
    width: 320px;
    height: 165px;
    background: radial-gradient(ellipse at 50% 55%, var(--logo-mid), var(--logo-top) 75%);
    display: flex;
    align-items: center;
    justify-content: center;
    gap: 10px;
  }
  .ad__logo-mark {
    width: 14px;
    height: 14px;
    background: var(--ink-white);
  }
  .ad__logo-name {
    font-family: "Michroma", sans-serif;
    font-size: 22px;
    color: var(--ink-white);
    letter-spacing: 1px;
  }
  .ad__headline {
    position: absolute;
    left: 0;
    right: 0;
    top: 518px;
    margin: 0;
    text-align: center;
    font-family: "Michroma", sans-serif;
    font-weight: 400;
    font-size: 38px;
    letter-spacing: 3px;
    color: var(--ink-white);
    -webkit-text-stroke: 1px var(--ink-white);
  }
  .ad__tagline {
    position: absolute;
    left: 0;
    right: 0;
    top: 602px;
    margin: 0;
    text-align: center;
    font-family: "Michroma", sans-serif;
    font-size: 22px;
    letter-spacing: 5px;
    color: var(--ink-white);
  }
  .ad__footer {
    position: absolute;
    left: 0;
    right: 0;
    bottom: 0;
    height: 128px;
    background: var(--band-dark);
    display: flex;
    align-items: center;
    justify-content: center;
  }
  .ad__url {
    font-family: "Open Sans", sans-serif;
    font-weight: 600;
    font-size: 31px;
    letter-spacing: 11px;
    color: var(--ink-white);
  }
</style>
</head>
<body>
  <main class="ad">
    <div class="ad__photo" role="img" aria-label="Photo of a narrow cobbled old-town street at dusk with warm street lamps, pastel buildings, a wooded hill behind, and a blurred cyclist riding past"></div>
    <div class="ad__logo-box">
      <span class="ad__logo-mark"></span>
      <span class="ad__logo-name">BRINDLEQUEST</span>
    </div>
    <h1 class="ad__headline">BRINDLEQUEST TOURS</h1>
    <p class="ad__tagline">CLIMBING + RIDING</p>
    <footer class="ad__footer">
      <span class="ad__url">www.brindlequest.com</span>
    </footer>
  </main>
</body>
</html>
```